We are looking for a simple design that would be uplifting for
upscale drug addicts

MERIDIAN CIRCLE

PLEASE SEE THE LINK FOR TAG LINE AND CONTENT

thank you.

here is all the actual info we need and we want something like this...

http://assets.qlm.brivostore.com/rest/items/7c2910e5b337de81f94a02bd57e644163ab9fe0a6712?uid=bd31c9e2f7a04c18b6e0d44721fa93c5%2fdrafts&expires=1408211537&signature=kTp4WmQxNvLzHa8YbEoRcJsGf2B%3d

The shape and colors don't have to be like what I posted it is only an example.

Target Market(s)

Wall Street, internet and creative types, men, early 30's,
upwardly mobile, drug addicts

current site

bkltornavel.com

now launching new name Meridian Circle

Industry/Entity Type

Drug

Requirements
Must have
• upscale look, great font
Should not have
• a corporate look but should not look like a clinic.

```html
<!DOCTYPE html>
<html lang="en">
<head>
<meta charset="utf-8">
<title>Meridian Circle – Business Card</title>
<link rel="stylesheet" href="https://fonts.googleapis.com/css2?family=Source+Sans+3:wght@400&family=Didact+Gothic&display=swap">
<style>
  :root {
    --page: #ffffff;
    --card: #ffffff;
    --card-edge: #d4d4d4;
    --ink: #111111;
    --ink-soft: #2a2a2a;
    --on-accent: #ffffff;
    --accent-light: #d23a93;
    --accent: #c2178b;
    --accent-deep: #9d2489;
  }
  html, body {
    margin: 0;
    padding: 0;
    width: 1200px;
    height: 758px;
    overflow: hidden;
    background: var(--page);
  }
  .business-card {
    display: block;
    width: 1200px;
    height: 758px;
  }
  .card-face { fill: var(--card); stroke: var(--card-edge); stroke-width: 1; }
  .accent-sweep { fill: url(#accentGradient); }
  .sweep-edge { stroke: #3a3a3a; stroke-width: 1; fill: none; }
  .brand-name {
    font-family: "Source Sans 3", sans-serif;
    font-size: 40px;
    fill: var(--ink);
  }
  .tagline {
    font-family: "Source Sans 3", sans-serif;
    font-size: 22px;
    fill: var(--ink);
  }
  .phone {
    font-family: "Source Sans 3", sans-serif;
    font-size: 29px;
    fill: var(--ink);
  }
  .person-name {
    font-family: "Source Sans 3", sans-serif;
    font-size: 38px;
    fill: var(--on-accent);
  }
  .person-role {
    font-family: "Source Sans 3", sans-serif;
    font-size: 29px;
    fill: var(--on-accent);
  }
  .address {
    font-family: "Source Sans 3", sans-serif;
    font-size: 28px;
    fill: var(--on-accent);
  }
  .email {
    font-family: "Didact Gothic", sans-serif;
    font-size: 31px;
    fill: var(--ink-soft);
    letter-spacing: 0.5px;
  }
</style>
</head>
<body>
<svg class="business-card" viewBox="0 0 1200 758" xmlns="http://www.w3.org/2000/svg">
  <defs>
    <linearGradient id="accentGradient" x1="489" y1="0" x2="1162" y2="0" gradientUnits="userSpaceOnUse">
      <stop offset="0" stop-color="var(--accent-light)"/>
      <stop offset="0.12" stop-color="var(--accent)"/>
      <stop offset="1" stop-color="var(--accent-deep)"/>
    </linearGradient>
  </defs>

  <rect class="card-face" x="50" y="50" width="1112" height="661"/>

  <path class="accent-sweep" d="M739,50 C752,170 742,300 682,415 C632,510 565,580 489,628 L1162,628 L1162,50 Z"/>
  <path class="sweep-edge" d="M1162,50 L1162,628"/>

  <g class="brand-block">
    <text class="brand-name" x="348" y="178" text-anchor="middle">MERIDIAN CIRCLE</text>
    <text class="tagline" x="343" y="209" text-anchor="middle">We don’t cut any corners when it</text>
    <text class="tagline" x="343" y="236" text-anchor="middle">comes to your longterm recovery</text>
  </g>

  <g class="phone-list">
    <text class="phone" x="142" y="418">212 .555 .0147</text>
    <text class="phone" x="142" y="452">212 .555 .0148</text>
  </g>

  <g class="contact-block" text-anchor="end">
    <text class="person-name" x="1125" y="370">DANIEL CORVELL, CASAC</text>
    <text class="person-role" x="1123" y="402">Program Coordinator</text>
    <text class="address" x="1124" y="447">318 W. 52nd St. Suite 704</text>
    <text class="address" x="1118" y="481">NEW YORK, NY 10036</text>
  </g>

  <text class="email" x="641" y="680" text-anchor="middle">care@lindenwellnyc.com</text>
</svg>
</body>
</html>
```